Create a landing page for my local business that I’m looking to advertise

I own an oriental rug repair, restoration and cleaning business.
I’m looking to rug advertising and i would like a very clear *******UX and UI design******* website designed.

pages that i need:
-Repair and restoration
-Cleaning
-Blocking
-Staircase rug installation
_about us
-homepage
-our story
-contact us
-estimate

Www.velorantex.com

Industry/Entity Type

Rug Industry, Antique and New Rug Repair restoration and cleaning

Number of Pages Required

5+ page

Font styles to use
Serif
Sans Serif
Script

Colors
6B429C
8869AF
B7A5CE
E3DAEB
F3F0F8

Requirements
Must have
• IT HAS TO PRESENT FINE RUG REPAIR, RESTORATION AND CLEANING.
Should not have
• I DONT WANT THE WEBSITE TO LOOK LIKE A GENERIC “CLEANING COMPANY”. WE ARE A HIGH END RUG REPAIR ,RESTORATION AND CLEANING COMPANY

```html
<!DOCTYPE html>
<html lang="en">
<head>
<meta charset="utf-8">
<title>Velorantex Rug – Oriental Rug Repair, Restoration &amp; Cleaning</title>
<link rel="stylesheet" href="https://fonts.googleapis.com/css2?family=Cormorant+Garamond:wght@500;600&family=Lato:wght@400;700&family=Montserrat:wght@500;600&display=swap">
<style>
:root{
  --purple:#6B429C;
  --purple-mid:#8869AF;
  --purple-soft:#B7A5CE;
  --purple-pale:#E3DAEB;
  --purple-mist:#F3F0F8;
  --ink:#333;
  --heading:#2a2a2a;
  --footer:#1c1b1d;
  --white:#fff;
}
*{box-sizing:border-box;margin:0;padding:0}
html,body{width:1200px;height:3871px;overflow:hidden}
body{position:relative;font-family:'Lato',sans-serif;color:var(--ink);background:var(--white)}
.abs{position:absolute}
.serif{font-family:'Cormorant Garamond',serif;text-transform:uppercase;font-weight:600;letter-spacing:1px}
.btn{position:absolute;display:flex;align-items:center;justify-content:center;border-radius:24px;
  background:linear-gradient(90deg,var(--purple-mid),var(--purple));color:var(--white);
  font-family:'Cormorant Garamond',serif;font-weight:600;text-transform:uppercase;font-size:16px;letter-spacing:.5px}
.center{text-align:center}

/* top bar */
.topbar{left:0;top:0;width:1200px;height:39px;background:var(--purple);color:var(--white);
  font-family:'Montserrat',sans-serif;font-size:12px}
.topbar span{position:absolute;top:12px}
.topbar .sep{position:absolute;top:4px;width:1px;height:30px;background:rgba(255,255,255,.5)}
.topbar .ico{position:absolute;top:13px;width:12px;height:12px;border-radius:50%;background:var(--white)}

/* hero */
.hero{left:0;top:39px;width:1200px;height:659px;
  background:radial-gradient(ellipse at 50% 55%,#9a6a3c 0%,#6e3c22 40%,#3a1e12 80%),#4a2616}
.brand{left:0;top:60px;width:1200px;text-align:center;color:var(--white);white-space:nowrap}
.brand .name{font-family:'Cormorant Garamond',serif;font-size:36px;font-weight:600;letter-spacing:1px;line-height:1}
.brand .tag{font-family:'Cormorant Garamond',serif;font-size:9px;letter-spacing:3px;margin-top:4px}
.nav{left:0;top:119px;width:1200px;font-family:'Montserrat',sans-serif;font-size:12px;font-weight:600;color:var(--white)}
.nav span{position:absolute}
.hero-box{left:207px;top:248px;width:786px;height:360px;background:rgba(60,40,30,.55)}
.hero-title{left:0;top:283px;width:1200px;font-size:68px;color:var(--white);font-weight:500;letter-spacing:2px}
.hero-text{left:250px;top:366px;width:700px;color:var(--white);font-size:15px;line-height:28px}
.dots{left:567px;top:631px}
.dots i{display:inline-block;width:12px;height:12px;border:1.5px solid var(--white);border-radius:50%;margin-right:5px}
.dots i:first-child{background:var(--white)}

/* services */
.h2{position:absolute;left:0;width:1200px;text-align:center;font-size:32px;color:var(--heading)}
.rule{position:absolute;left:577px;width:46px;height:3px;background:var(--purple)}
.intro{left:190px;top:832px;width:820px;font-size:13px;line-height:28px}
.photo{position:absolute;width:455px;height:319px}
.photo::after{content:"";position:absolute;left:10px;top:10px;right:10px;bottom:10px;border:1.5px solid rgba(255,255,255,.9)}
.card-title{position:absolute;width:455px;text-align:center;font-size:23px;color:var(--heading)}
.card-text{position:absolute;width:435px;text-align:center;font-size:13px;line-height:28px}

/* about band */
.about{left:0;top:2068px;width:1200px;height:485px;background:linear-gradient(90deg,var(--purple-mid),var(--purple))}
.about-text{left:185px;top:2208px;width:830px;color:var(--white);font-size:13px;line-height:28px}
.btn-white{background:var(--white);color:var(--purple)}

/* split */
.split-h{position:absolute;font-size:33px;color:var(--heading);line-height:38px;font-weight:500}
.split-text{position:absolute;font-size:13px;line-height:28px;width:490px}

/* footer */
.footer{left:0;top:3435px;width:1200px;height:436px;background:var(--footer);color:var(--white)}
.f-h{position:absolute;top:3501px;font-family:'Cormorant Garamond',serif;font-size:15px;font-weight:600;text-transform:uppercase;letter-spacing:.5px;color:var(--white)}
.f-links{position:absolute;left:413px;top:3536px;font-size:14px;line-height:28px;color:var(--white)}
.f-row{position:absolute;display:flex;align-items:center;font-size:14px;color:var(--white);white-space:nowrap}
.f-row .c{width:30px;height:30px;border-radius:50%;background:var(--purple-mid);margin-right:20px;display:flex;align-items:center;justify-content:center}
.f-line{left:120px;top:3770px;width:952px;height:1px;background:rgba(255,255,255,.4)}
.copy{left:0;top:3799px;width:1200px;text-align:center;font-size:12px;color:var(--white)}
</style>
</head>
<body>

<header>
  <div class="abs topbar">
    <span style="left:128px">&#9742; (555)014-2270</span>
    <div class="sep" style="left:260px"></div>
    <span style="left:273px">&#9993; info@velorantex.com</span>
    <div class="sep" style="left:450px"></div>
    <span style="left:466px">&#9906; 1480 Marlow Ave, Brennan, IL 60099</span>
    <div class="sep" style="left:940px"></div>
    <i class="ico" style="left:970px"></i>
    <i class="ico" style="left:997px"></i>
    <i class="ico" style="left:1025px"></i>
    <svg class="abs" style="left:1057px;top:12px" width="16" height="14" viewBox="0 0 16 14"><path d="M1 1h3l2 8h8l1-6H5" fill="none" stroke="#fff" stroke-width="1.6"/><circle cx="7" cy="12" r="1.4" fill="#fff"/><circle cx="13" cy="12" r="1.4" fill="#fff"/></svg>
  </div>

  <div class="abs hero" role="img" aria-label="Photograph looking down a curved staircase fitted with a red and gold oriental stair runner"></div>

  <div class="abs brand">
    <div class="name">VELORANTEX RUG</div>
    <div class="tag">REPAIR | RESTORATION | CLEANING</div>
  </div>
  <div class="btn" style="left:825px;top:54px;width:243px;height:45px">Get a Free Estimate</div>

  <nav class="abs nav">
    <span style="left:120px">HOME</span>
    <span style="left:205px">ABOUT US</span>
    <span style="left:316px">REPAIR AND RESTORATION</span>
    <span style="left:535px">CLEANING</span>
    <span style="left:647px">BLOCKING</span>
    <span style="left:760px">STAIRCASE RUG INSTALLATION</span>
    <span style="left:999px">CONTACT US</span>
  </nav>

  <div class="abs hero-box"></div>
  <h1 class="abs hero-title serif center">Oriental Rug Repair</h1>
  <p class="abs hero-text center">Velorantex Rug is a leading and trusted brand for all oriental and antique rug repairs, not only by consumers, but by all Chicagoland's finest Oriental Rug dealers and designers. With more than 30-plus years of experience.</p>
  <div class="btn" style="left:479px;top:469px;width:242px;height:45px">Get a Free Estimate</div>
  <div class="abs dots"><i></i><i></i><i></i><i></i></div>
</header>

<section class="services">
  <h2 class="h2 serif" style="top:766px">Our Services</h2>
  <div class="rule" style="top:815px"></div>
  <p class="abs intro center">At Velorantex Rug, we strive to keep your home looking its best. That means our team is ready to help you with everything from oriental rug cleaning to sun fade or color correction, minor or major repair etc.</p>

  <div class="photo" style="left:129px;top:927px;background:linear-gradient(135deg,#8a3a2c,#c9a88a 50%,#5a2a24)" role="img" aria-label="Close-up of a worn antique rug edge with loose fringe awaiting repair"></div>
  <h3 class="card-title serif" style="left:129px;top:1267px">Antique Rug Repair</h3>
  <p class="card-text" style="left:139px;top:1302px">Our Antique Rug Repair can help you improve your customer retention rate by giving you access to our team of expert weavers who are trained in various kinds of repairs, such as re-surging area rug.</p>
  <div class="btn" style="left:271px;top:1398px;width:173px;height:45px">Learn More</div>

  <div class="photo" style="left:613px;top:927px;background:linear-gradient(180deg,#6a4a3a,#5a1e1e 50%,#e8e4e0)" role="img" aria-label="Dark red oriental runner installed on a white staircase"></div>
  <h3 class="card-title serif" style="left:613px;top:1267px">Oriental Rug Restoration</h3>
  <p class="card-text" style="left:623px;top:1302px">There are a variety of different reasons why rugs may need repair. Rugs, like anything else in your home, will eventually show signs of wear and tear. Even if you think that the rug is irreparable.</p>
  <div class="btn" style="left:755px;top:1398px;width:173px;height:45px">Learn More</div>

  <div class="photo" style="left:129px;top:1470px;background:linear-gradient(90deg,#9a3a2a,#6a4a3a 55%,#3a3634)" role="img" aria-label="Freshly cleaned tribal rug laid on a dark wood floor with a tag attached"></div>
  <h3 class="card-title serif" style="left:129px;top:1810px">Antique Rug Cleaning</h3>
  <p class="card-text" style="left:139px;top:1845px">Oriental rugs are a beautiful and integral part of any interior. They feel nice to walk on and look great by brightening other pieces of furniture in the room. A handmade oriental rug is a piece of art.</p>
  <div class="btn" style="left:271px;top:1942px;width:173px;height:45px">Learn More</div>

  <div class="photo" style="left:613px;top:1470px;background:radial-gradient(circle at 50% 35%,#d8c4a8 0 10%,#6a2424 30%,#3a1416)" role="img" aria-label="Red Persian rug with a hole being rewoven"></div>
  <h3 class="card-title serif" style="left:613px;top:1810px">Staircase Rug Installation</h3>
  <p class="card-text" style="left:623px;top:1845px">One of our specialties is installing handmade rugs on staircases. Our team will come out and measure the staircase, take into account any obstacles like railings or banisters, and customize the rug.</p>
  <div class="btn" style="left:755px;top:1942px;width:173px;height:45px">Learn More</div>
</section>

<section>
  <div class="abs about"></div>
  <h2 class="h2 serif" style="top:2142px;color:var(--white)">About Velorantex Rug</h2>
  <div class="rule" style="top:2191px;background:var(--white)"></div>
  <p class="abs about-text center">Velorantex Rug is a leading and trusted brand for all oriental and antique rug repairs, not only by consumers, but by all Chicagoland's finest Oriental Rug dealers and designers. With more than 30-plus years of experience, we are proud to offer a wide range of services for all types of rugs, including fine Persian rugs, Afghan rugs, Pakistani rugs, wool rugs, Antique Rugs, Oriental Rugs, Shag and many others across the United States and all over the world. Our repair, restoration and cleaning team specializes in high-quality antique rug restoration and repair, as well as wool &amp; silk rugs, from all over the world. Sometimes wear and tear can happen in high traffic areas, or can be damaged by your beloved dogs or cats. Our team of experts will come to your home and assess your rug needs and either fix the problem on-site for you, or take it to our Brennan-based facility for any type of services your rug may need.</p>
  <div class="btn btn-white" style="left:479px;top:2424px;width:242px;height:44px">Get a Free Estimate</div>
</section>

<section>
  <div class="photo" style="left:105px;top:2631px;background:linear-gradient(180deg,#2a2a2c,#4a4a4c 60%,#c8c4be)" role="img" aria-label="Modern showroom office with desks, chairs and a light rug on the floor"></div>
  <h2 class="split-h serif" style="left:602px;top:2633px">There is nothing more<br>precious than the original.</h2>
  <div class="abs" style="left:602px;top:2719px;width:46px;height:3px;background:var(--purple)"></div>
  <p class="split-text" style="left:602px;top:2737px">We value authenticity and we built our name on restoring rugs by hand, bringing back to life and using pieces that are in your family for generations or that you invested in because you appreciate their craftsmanship. This is our contribution to keeping the authenticity in your homes, and teaching new generations about the value manual craftsmanship can build, to the state of calling it art.</p>
  <div class="btn" style="left:602px;top:2897px;width:244px;height:45px">Get a Free Estimate</div>

  <h2 class="split-h serif" style="left:108px;top:3024px">We care and respect the<br>rugs we work on.</h2>
  <div class="abs" style="left:108px;top:3110px;width:46px;height:3px;background:var(--purple)"></div>
  <p class="split-text" style="left:108px;top:3128px">With over 30 years of expertise in restoring and cleaning precious rugs, we feel we have a duty to bring each rug to its former glory whenever this is possible. We are a family-owned and -operated area rug repair and restoration firm near Chicago, specializing in Oriental Rug Cleaning, Antique Rug Repair, Sun Fade Damage, Rug Stain Removal and many more services.</p>
  <div class="btn" style="left:108px;top:3289px;width:244px;height:45px">Get a Free Estimate</div>
  <div class="photo" style="left:637px;top:3023px;background:linear-gradient(135deg,#b8a88e,#d8ccb8 50%,#8a7a66)" role="img" aria-label="Hands restoring the worn back of a pale floral rug by hand"></div>
</section>

<footer>
  <div class="abs footer"></div>
  <div class="abs brand" style="left:90px;top:3593px;width:320px">
    <div class="name" style="font-size:30px">VELORANTEX RUG</div>
    <div class="tag">REPAIR | RESTORATION | CLEANING</div>
  </div>

  <h4 class="f-h" style="left:413px">Quick Links</h4>
  <div class="f-links">Home<br>About Us<br>Repair and restoration<br>Cleaning<br>Blocking<br>Staircase rug installation<br>Contact Us</div>

  <h4 class="f-h" style="left:605px">Follow Us</h4>
  <div class="f-row" style="left:605px;top:3539px"><span class="c"></span>Community</div>
  <div class="f-row" style="left:605px;top:3585px"><span class="c"></span>Gallery</div>
  <div class="f-row" style="left:605px;top:3633px"><span class="c"></span>Updates</div>
  <div class="f-row" style="left:605px;top:3680px"><span class="c"></span>Network</div>

  <h4 class="f-h" style="left:799px">Contact Us</h4>
  <div class="f-row" style="left:799px;top:3539px"><span class="c"><svg width="12" height="14" viewBox="0 0 12 14"><path d="M6 13S1 8 1 5a5 5 0 0110 0c0 3-5 8-5 8z" fill="#fff"/><circle cx="6" cy="5" r="1.8" fill="#8869AF"/></svg></span>1480 Marlow Ave, Brennan, IL 60099</div>
  <div class="f-row" style="left:799px;top:3593px"><span class="c"><svg width="12" height="12" viewBox="0 0 12 12"><path d="M2 1l2 0 1 3-1.5 1a7 7 0 003.5 3.5L8 7l3 1v2c0 1-1 1-1 1C5 11 1 7 1 2c0 0 0-1 1-1z" fill="#fff"/></svg></span>(555)014-2270</div>
  <div class="f-row" style="left:799px;top:3646px"><span class="c"><svg width="12" height="12" viewBox="0 0 12 12"><rect x="1" y="4" width="10" height="6" fill="#fff"/><rect x="3" y="1" width="6" height="3" fill="#fff"/></svg></span>55555555555</div>
  <div class="f-row" style="left:799px;top:3699px"><span class="c"><svg width="12" height="10" viewBox="0 0 12 10"><rect x="0.5" y="0.5" width="11" height="9" fill="#fff"/><path d="M1 1l5 4 5-4" fill="none" stroke="#8869AF"/></svg></span>info@velorantex.com</div>

  <div class="abs f-line"></div>
  <p class="abs copy">© Copyright 2021 Velorantex Rug - All rights reserved</p>
</footer>

</body>
</html>
```